Brackenridge Strength Studio Chronic Pain Flyer

Double sided DL flyer required to promote a strength training studio to sufferers of chronic pain. Flyer will be displayed in osteopathy, chiropractic and massage clinics. Flyer should be clean, professional and appeal to an older (40+) demographic.

Target Market(s)

Chronic pain sufferers. Age 40+

Industry/Entity Type

Health And Wellness

Colors

Designer to choose colors to be used in the design.

Requirements
Must have
• See attached files for text copy and logo. Image(s) of people strength training with a coach or personal trainer, as well as images depicting pain in common parts of the body (such as those pictured in the supplied mock up)
• website address: brackenridgestrengthstudio.example.com.au
• phone number : 0452 918 304
• Street address: 4/63 Juniper Hollow Rd, Brackenridge
Nice to have
• Images such as in the attached files.

```html
<!DOCTYPE html>
<html lang="en">
<head>
<meta charset="utf-8">
<title>Brackenridge Strength Studio – Chronic Pain Flyer</title>
<link href="https://fonts.googleapis.com/css2?family=Oswald:wght@500;700&family=Montserrat:wght@600;700&family=Questrial&display=swap" rel="stylesheet">
<style>
  :root{
    --red:#e3303f;
    --red-deep:#b81f2c;
    --charcoal:#3b3c3f;
    --ink:#161616;
    --paper:#ffffff;
    --mist:#ededee;
    --backdrop:#e6e6e7;
    --logo-grey:#6d6e71;
  }
  *{box-sizing:border-box;margin:0;padding:0}
  html,body{width:1200px;height:1000px;overflow:hidden}
  body{background:var(--backdrop);position:relative;font-family:"Questrial",sans-serif}

  .flyer{position:absolute;top:70px;width:410px;height:860px;background:var(--paper);overflow:hidden;box-shadow:0 4px 14px rgba(0,0,0,.12)}
  .flyer--front{left:165px}
  .flyer--back{left:625px}

  .brand{position:absolute;left:0;right:0;text-align:center;font-family:"Montserrat",sans-serif;font-weight:700;color:var(--logo-grey);line-height:1.05;letter-spacing:1px}
  .brand__name{display:block;font-size:34px}
  .brand__sub{display:block;font-size:19px;letter-spacing:3px}

  .headline{position:absolute;font-family:"Oswald",sans-serif;text-transform:uppercase;line-height:.95;text-align:center}
  .headline__lead{display:block;color:var(--ink);font-weight:700;font-size:36px;letter-spacing:-.5px}
  .headline__main{display:block;color:var(--red);font-weight:700;font-size:66px;letter-spacing:-1px}

  /* front */
  .front__panel{position:absolute;left:0;top:118px;right:0;bottom:0;background:var(--charcoal)}
  .front__stage{position:absolute;left:62px;top:150px;right:0;bottom:0;background:var(--mist);border-top-left-radius:260px 220px}
  .front .headline{left:80px;right:0;top:162px}
  .front__photo{position:absolute;left:96px;top:290px;right:0;bottom:120px;border-top-left-radius:120px;
    background:linear-gradient(160deg,#d9d9da 0%,#b9b2ac 35%,#7a5f52 55%,#2a2a2c 80%,#b6232e 100%)}
  .pain-spot{position:absolute;left:14px;width:124px;height:124px;border-radius:50%;border:3px solid var(--paper);box-shadow:0 0 0 3px var(--red);
    background:radial-gradient(circle at 55% 55%,#e5606b 0%,#d7a4a4 22%,#cfcfcf 48%,#9c9c9c 100%)}
  .pain-spot--back{top:312px}
  .pain-spot--shoulder{top:452px}
  .pain-spot--knee{top:594px}

  .contact-band{position:absolute;left:0;right:0;bottom:0}
  .contact-band svg{display:block;width:100%}
  .contact{position:absolute;left:0;right:0;color:var(--paper);font-family:"Montserrat",sans-serif;text-align:center}
  .contact__phone{font-size:40px;font-weight:700;letter-spacing:1px}
  .contact__line{font-size:14px;font-weight:600;margin-top:5px}

  /* back */
  .back__photo{position:absolute;left:0;top:0;width:410px;height:175px}
  .back .brand{top:192px}
  .back .headline{left:0;right:0;top:268px}
  .tagline{position:absolute;left:0;right:0;top:395px;text-align:center;font-family:"Oswald",sans-serif;font-weight:500;font-size:15px;letter-spacing:.5px;color:var(--ink);text-transform:uppercase}
  .body-copy{position:absolute;left:30px;right:30px;top:425px;font-size:15.5px;line-height:1.32;color:var(--ink);text-align:justify}
  .body-copy p+p{margin-top:16px}
  .body-copy .cta{color:var(--red);font-weight:700}
</style>
</head>
<body>

<section class="flyer flyer--front front" aria-label="Flyer front">
  <div class="brand" style="top:30px">
    <span class="brand__name">BRACKENRIDGE</span>
    <span class="brand__sub">STRENGTH STUDIO</span>
  </div>
  <div class="front__panel"></div>
  <div class="front__stage"></div>
  <div class="front__photo" role="img" aria-label="Smiling woman lifting a barbell with a personal trainer guiding her"></div>
  <h1 class="headline">
    <span class="headline__lead">Health Through</span>
    <span class="headline__main">Strength</span>
  </h1>
  <div class="pain-spot pain-spot--back" role="img" aria-label="Lower back with highlighted area of pain"></div>
  <div class="pain-spot pain-spot--shoulder" role="img" aria-label="Shoulder with highlighted area of pain"></div>
  <div class="pain-spot pain-spot--knee" role="img" aria-label="Knee held in hands with highlighted area of pain"></div>

  <div class="contact-band" style="height:200px">
    <svg viewBox="0 0 410 200" width="410" height="200" aria-hidden="true">
      <path d="M0 38 C110 5 250 70 410 20 L410 200 L0 200Z" fill="var(--charcoal)"/>
      <path d="M0 44 C110 12 250 78 410 28 L410 200 L0 200Z" fill="var(--red)"/>
    </svg>
    <div class="contact" style="top:62px">
      <div class="contact__phone">0452 918 304</div>
      <div class="contact__line">info@brackenridgestrengthstudio.example.com.au</div>
      <div class="contact__line" style="font-size:17px">4/63 Juniper Hollow Rd, Brackenridge</div>
    </div>
  </div>
</section>

<section class="flyer flyer--back back" aria-label="Flyer back">
  <svg class="back__photo" viewBox="0 0 410 175" width="410" height="175" role="img" aria-label="Trainer spotting a woman pressing dumbbells on a bench">
    <defs>
      <linearGradient id="gymTone" x1="0" y1="0" x2="1" y2="1">
        <stop offset="0" stop-color="#9c9a98"/>
        <stop offset=".5" stop-color="#4a4849"/>
        <stop offset="1" stop-color="#1f1f21"/>
      </linearGradient>
    </defs>
    <path d="M0 0 H410 V150 C300 178 140 178 0 132Z" fill="var(--charcoal)"/>
    <path d="M0 0 H410 V140 C300 168 140 165 0 122Z" fill="url(#gymTone)"/>
  </svg>
  <div class="brand">
    <span class="brand__name">BRACKENRIDGE</span>
    <span class="brand__sub">STRENGTH STUDIO</span>
  </div>
  <h2 class="headline">
    <span class="headline__lead">Health Through</span>
    <span class="headline__main">Strength</span>
  </h2>
  <p class="tagline">You don't have to live in pain</p>
  <div class="body-copy">
    <p>Strength training has been shown to improve many chronic pain conditions and is now being routinely recommended by medical and health professionals</p>
    <p>Our private studio provides high quality strength training by expert strength coaches. We've helped countless people improve or eliminate chronic pain, <span class="cta">contact us today and find out how we can help you.</span></p>
  </div>

  <div class="contact-band" style="height:210px">
    <svg viewBox="0 0 410 210" width="410" height="210" aria-hidden="true">
      <path d="M0 34 C120 10 250 55 410 14 L410 210 L0 210Z" fill="var(--charcoal)"/>
      <path d="M0 40 C120 16 250 62 410 20 L410 210 L0 210Z" fill="var(--red)"/>
    </svg>
    <div class="contact" style="top:66px">
      <div class="contact__phone">0452 918 304</div>
      <div class="contact__line">info@brackenridgestrengthstudio.example.com.au</div>
      <div class="contact__line" style="font-size:17px">4/63 Juniper Hollow Rd, Brackenridge</div>
    </div>
  </div>
</section>

</body>
</html>
```